Opening Titles for "Harrow's Lantern" - Social Justice Feature Film

We are looking for a designer to design the opening titles for our social justice film "Harrow's Lantern.” "Harrow's Lantern" is the story of a separated mixed status and mixed ethnic family and their journey to reunite. You can see an early teaser of the film here (https://kmtrzo.files.example/s/b52kd9wqxe318pn7c20tfhsz4g8m1x6j)(please note this is a TEASER NOT a trailer - it shows the story of only one of the family members in the teaser not all of them).
There is a mood board attached here that can help explain what we are looking for. A few things to keep in mind:
- We would like the Main Title "HARROW'S LANTERN," to be in block letters with illustrated images that represent the town that two of the characters emigrate from and the culture/family life inside of the letters. "HARROW'S LANTERN" title should be reminiscent of a particular kind of storytelling that comes from the coast of Oaxaca and Guerrero, particularly in the Afro-Mexico culture where we can see the storytelling in the artifacts as illustrated in the board. The images on the circle and the flsh plates are not just images, they are also telling a story and are reflective of a particular community. In the case of the film, at the start of the story, this family comes from an Afro-Mexican community.
- Please note where it says to double click on an image as that will lead to free ReelBarn videos that will give you a deeper sense of what we are looking for.
- As for the lettering of the titles/credits, with the exception of “HARROW’S LANTERN” the font of everything else should look in the style of the “Brindle Parlour Script” lettering.
- Each credit name/title should be in a different color that works well with the background image. A good example of this is the color of the credit with the woman in the hammock. (timecode: 1:01:20:18 in the Opening Credits/Titles clip: https://clipvault.example/7RqTuNbK ). In this clip you can see that the yellow of the letters brings out the yellows and greens of the image behind it.
- Around each Credit name please frame it (however you choose to frame them) with a piece(s) of Mexican tile. The tile ideas are in the mood board and you can see something similar in the opening credits for “Under a Copper Sky” with the multicolored triangles. Double click on it in the mood board to see the “Under a Copper Sky” opening credits.
Here is a clip of the opening credits so that you can see where your design will go and how it will be used: https://clipvault.example/7RqTuNbK

```html
<!DOCTYPE html>
<html lang="en">
<head>
<meta charset="utf-8">
<title>Harrow's Lantern — Opening Titles</title>
<link rel="stylesheet" href="https://fonts.googleapis.com/css2?family=Bowlby+One&family=Londrina+Solid:wght@400;900&family=Cabin+Condensed:wght@500&display=swap">
<style>
:root{
  --paper:#ffffff;
  --outline:#4a2a1a;
  --ochre:#c98f4e;
  --teal:#3f7a84;
  --gold:#c8842e;
  --navy:#2e3f66;
  --rose:#c8506a;
  --mustard:#a88a1e;
  --coral:#d9703e;
  --slate:#6a7fa8;
  --violet:#8a72c8;
  --azure:#3a7ccc;
  --clay:#c26a4e;
  --berry:#c24e5e;
  --label-ink:#c7a27a;
}
*{margin:0;padding:0;box-sizing:border-box}
html,body{width:751px;height:1200px;overflow:hidden;background:var(--paper)}
.canvas{position:relative;width:751px;height:1200px;background:var(--paper)}
.main-title{position:absolute;left:0;top:0;width:751px;height:300px}
.main-title text{font-family:"Bowlby One",sans-serif;stroke:var(--outline);stroke-width:2;paint-order:stroke fill}
.label{font-family:"Cabin Condensed",sans-serif;font-weight:500;color:var(--label-ink);
  -webkit-text-stroke:0.6px var(--outline);position:absolute;white-space:nowrap;line-height:1}
.name{font-family:"Londrina Solid",sans-serif;font-weight:900;position:absolute;white-space:nowrap;
  line-height:1;-webkit-text-stroke:1.4px var(--outline);paint-order:stroke fill;letter-spacing:0.5px}
.tile-strip{position:absolute;height:7px;border-radius:4px;opacity:.85}
</style>
</head>
<body>
<main class="canvas">
  <svg class="main-title" viewBox="0 0 751 300" role="img" aria-label="HARROW'S LANTERN block letters, each filled with illustrations of a coastal hometown, sea, hills, city and family life">
    <defs>
      <linearGradient id="title-fill-one" x1="112" y1="0" x2="645" y2="0" gradientUnits="userSpaceOnUse">
        <stop offset="0" stop-color="#8a5a3a"/>
        <stop offset=".22" stop-color="#38b8c8"/>
        <stop offset=".4" stop-color="#6a8a5a"/>
        <stop offset=".52" stop-color="#7a8ab8"/>
        <stop offset=".65" stop-color="#e0702a"/>
        <stop offset=".8" stop-color="#4ab8a8"/>
        <stop offset="1" stop-color="#3a6a4a"/>
      </linearGradient>
      <linearGradient id="title-fill-two" x1="172" y1="0" x2="590" y2="0" gradientUnits="userSpaceOnUse">
        <stop offset="0" stop-color="#3a8ad0"/>
        <stop offset=".2" stop-color="#e0a040"/>
        <stop offset=".45" stop-color="#2a3a5a"/>
        <stop offset=".62" stop-color="#e0c040"/>
        <stop offset=".78" stop-color="#c0403a"/>
        <stop offset="1" stop-color="#6ab04a"/>
      </linearGradient>
    </defs>
    <text x="112" y="198" font-size="106" textLength="533" lengthAdjust="spacingAndGlyphs" fill="url(#title-fill-one)">HARROW'S</text>
    <text x="172" y="283" font-size="108" textLength="418" lengthAdjust="spacingAndGlyphs" fill="url(#title-fill-two)">LANTERN</text>
  </svg>

  <!-- production company -->
  <span class="name" style="left:217px;top:385px;font-size:26px;color:var(--ochre)">A</span>
  <span class="tile-strip" style="left:116px;top:396px;width:90px;background:linear-gradient(90deg,#c98f4e,#d9703e,#c98f4e)" role="img" aria-label="tile ornament row"></span>
  <span class="tile-strip" style="left:244px;top:396px;width:90px;background:linear-gradient(90deg,#c98f4e,#d9703e,#c98f4e)" role="img" aria-label="tile ornament row"></span>
  <span class="name" style="left:114px;top:412px;font-size:27px;color:var(--ochre)">TALLOW WORKS</span>
  <span class="tile-strip" style="left:114px;top:456px;width:34px;background:var(--coral)" role="img" aria-label="tile ornament"></span>
  <span class="name" style="left:155px;top:446px;font-size:27px;color:var(--ochre)">PRODUCTION</span>
  <span class="tile-strip" style="left:302px;top:456px;width:34px;background:var(--coral)" role="img" aria-label="tile ornament"></span>

  <!-- collaboration -->
  <span class="label" style="left:450px;top:378px;font-size:21px">In Collaboration</span>
  <span class="label" style="left:500px;top:400px;font-size:21px">With</span>
  <span class="tile-strip" style="left:424px;top:408px;width:70px;background:linear-gradient(90deg,#c98f4e,#d9703e)" role="img" aria-label="tile ornament row"></span>
  <span class="tile-strip" style="left:548px;top:408px;width:72px;background:linear-gradient(90deg,#d9703e,#c98f4e)" role="img" aria-label="tile ornament row"></span>
  <span class="name" style="left:426px;top:424px;font-size:32px;color:var(--gold)">VERANDA FILMS</span>
  <span class="tile-strip" style="left:424px;top:466px;width:196px;background:linear-gradient(90deg,#c98f4e,#d9703e,#c98f4e,#d9703e)" role="img" aria-label="tile ornament row"></span>

  <!-- principal cast -->
  <span class="name" style="left:74px;top:532px;font-size:28px;color:var(--teal)">IMARA</span>
  <span class="tile-strip" style="left:156px;top:536px;width:96px;background:var(--slate)" role="img" aria-label="tile ornament row"></span>
  <span class="tile-strip" style="left:72px;top:566px;width:82px;background:var(--slate)" role="img" aria-label="tile ornament row"></span>
  <span class="name" style="left:158px;top:550px;font-size:28px;color:var(--teal)">DELVECQ</span>

  <span class="name" style="left:296px;top:530px;font-size:26px;color:var(--gold)">TOMÁS</span>
  <span class="tile-strip" style="left:404px;top:540px;width:52px;background:var(--gold)" role="img" aria-label="tile ornament row"></span>
  <span class="tile-strip" style="left:298px;top:565px;width:52px;background:var(--gold)" role="img" aria-label="tile ornament row"></span>
  <span class="name" style="left:362px;top:553px;font-size:28px;color:var(--navy)">BERROCAL</span>

  <span class="name" style="left:520px;top:536px;font-size:28px;color:var(--rose)">JUNIE</span>
  <span class="tile-strip" style="left:606px;top:542px;width:52px;background:var(--rose)" role="img" aria-label="tile ornament row"></span>
  <span class="tile-strip" style="left:524px;top:570px;width:70px;background:var(--rose)" role="img" aria-label="tile ornament row"></span>
  <span class="name" style="left:608px;top:556px;font-size:28px;color:var(--rose)">PARK</span>

  <!-- introducing -->
  <span class="label" style="left:62px;top:636px;font-size:19px;color:#c9a0a8">Introducing</span>
  <span class="name" style="left:62px;top:662px;font-size:27px;color:var(--mustard)">ELIÁN</span>
  <span class="tile-strip" style="left:142px;top:672px;width:72px;background:var(--coral)" role="img" aria-label="tile ornament row"></span>
  <span class="tile-strip" style="left:64px;top:698px;width:58px;background:var(--coral)" role="img" aria-label="tile ornament row"></span>
  <span class="name" style="left:132px;top:686px;font-size:27px;color:var(--mustard)">NAVARRO</span>

  <!-- casting -->
  <span class="tile-strip" style="left:264px;top:645px;width:76px;background:var(--coral)" role="img" aria-label="tile ornament row"></span>
  <span class="label" style="left:346px;top:630px;font-size:22px">Casting</span>
  <span class="tile-strip" style="left:420px;top:645px;width:76px;background:var(--coral)" role="img" aria-label="tile ornament row"></span>
  <span class="name" style="left:275px;top:660px;font-size:28px;color:var(--coral)">BLANCA ORTUÑO</span>
  <span class="name" style="left:286px;top:692px;font-size:28px;color:var(--coral)">SELENA ARÁUZ</span>
  <span class="name" style="left:260px;top:724px;font-size:28px;color:var(--coral)">AMPARO REVENTLOW</span>
  <span class="tile-strip" style="left:262px;top:762px;width:236px;background:linear-gradient(90deg,#d9703e,#c98f4e,#d9703e,#c98f4e)" role="img" aria-label="tile ornament row"></span>

  <!-- production designer -->
  <span class="label" style="left:538px;top:638px;font-size:16px;color:#c9a0c0">Production Designer</span>
  <span class="name" style="left:538px;top:660px;font-size:28px;color:var(--mustard)">LUCÍA</span>
  <span class="tile-strip" style="left:628px;top:668px;width:48px;background:var(--coral)" role="img" aria-label="tile ornament row"></span>
  <span class="tile-strip" style="left:540px;top:696px;width:70px;background:var(--coral)" role="img" aria-label="tile ornament row"></span>
  <span class="name" style="left:620px;top:680px;font-size:28px;color:var(--mustard)">ROLDÁN</span>

  <!-- editor -->
  <span class="label" style="left:170px;top:792px;font-size:21px;color:#b0b8c8">Editor</span>
  <span class="name" style="left:168px;top:818px;font-size:28px;color:var(--slate)">RADEK</span>
  <span class="tile-strip" style="left:250px;top:828px;width:78px;background:var(--slate)" role="img" aria-label="tile ornament row"></span>
  <span class="tile-strip" style="left:172px;top:858px;width:62px;background:var(--slate)" role="img" aria-label="tile ornament row"></span>
  <span class="name" style="left:242px;top:846px;font-size:28px;color:var(--slate)">OLMOS</span>

  <!-- director of photography -->
  <span class="label" style="left:412px;top:796px;font-size:17px;color:#b0a0d8">Director of Photography</span>
  <span class="name" style="left:410px;top:818px;font-size:27px;color:var(--violet)">CRISTÓBAL</span>
  <span class="tile-strip" style="left:532px;top:830px;width:136px;background:var(--violet)" role="img" aria-label="tile ornament row"></span>
  <span class="tile-strip" style="left:416px;top:858px;width:70px;background:var(--violet)" role="img" aria-label="tile ornament row"></span>
  <span class="name" style="left:498px;top:846px;font-size:27px;color:var(--violet)">PEÑA MORILLO</span>

  <!-- executive producer -->
  <span class="label" style="left:126px;top:912px;font-size:21px;color:#b0b8c8">Executive Producer</span>
  <span class="name" style="left:124px;top:938px;font-size:30px;color:var(--azure)">ADELINA</span>
  <span class="tile-strip" style="left:272px;top:948px;width:70px;background:var(--azure)" role="img" aria-label="tile ornament row"></span>
  <span class="tile-strip" style="left:124px;top:978px;width:124px;background:var(--azure)" role="img" aria-label="tile ornament row"></span>
  <span class="name" style="left:262px;top:964px;font-size:30px;color:var(--azure)">SEGURA</span>

  <!-- producer -->
  <span class="label" style="left:424px;top:908px;font-size:21px">Producer</span>
  <span class="name" style="left:422px;top:934px;font-size:28px;color:var(--clay)">DORIAN</span>
  <span class="tile-strip" style="left:522px;top:944px;width:106px;background:var(--clay)" role="img" aria-label="tile ornament row"></span>
  <span class="tile-strip" style="left:426px;top:974px;width:52px;background:var(--clay)" role="img" aria-label="tile ornament row"></span>
  <span class="name" style="left:486px;top:962px;font-size:30px;color:var(--clay)">SALLOW</span>

  <!-- written, directed & produced -->
  <span class="label" style="left:234px;top:1036px;font-size:21px;color:#e0a0a8">Written, Directed &amp; Produced By</span>
  <span class="name" style="left:236px;top:1066px;font-size:38px;color:var(--berry)">IMARA</span>
  <span class="tile-strip" style="left:370px;top:1076px;width:148px;background:var(--berry)" role="img" aria-label="tile ornament row"></span>
  <span class="tile-strip" style="left:242px;top:1114px;width:108px;background:var(--berry)" role="img" aria-label="tile ornament row"></span>
  <span class="name" style="left:360px;top:1096px;font-size:40px;color:var(--berry)">DELVECQ</span>
</main>
</body>
</html>
```